Business Card Design Project - IT Company

CLOUD IT company working with medium to large corporate clients requires 2 sided Business Card design.

Strong, Professional and modern is what I am looking for.

The Logo JPG attached has all the colour palette options. which consist of Red and Silver on various backgrounds

Preferred option for the Back of card is either Silver Text on Red or Silver Text on Black. Though this is not concrete. Surprise me.

Logo must be prominent along with Contact details of the staff member

Tagline can be all Capitals " CLOUD MANAGED SERVICES"

I will look to provide feedback and tweaks to get the right design so it should be a fun process.

I will provide the layered files to the top few contenders.

Reason: Leaving the door open for some creativity. Don't forget this is an technology company. .

Target Market(s)

Leaders, decision makers, CEOs, CIOs,

Industry/Entity Type

Business

Requirements
Must have
• Data must have is

Company Name: Velquora
Tagline: Cloud Managed Services

No Particular order

First Name Last name
Director
Mobile 0452 987 654
www.velquora.com
First.Lastname@velquora.com
Suite 5, 48 Marlowe Lane, Sydney NSW 2000

```html
<!DOCTYPE html>
<html lang="en">
<head>
<meta charset="utf-8">
<title>Velquora — Business Card</title>
<link href="https://fonts.googleapis.com/css2?family=Open+Sans:wght@400;600;700&display=swap" rel="stylesheet">
<style>
  :root {
    --backdrop: #6b6b6b;
    --brand-red: #b01f28;
    --brand-red-dark: #8f1820;
    --silver: #dcdcdc;
    --card-white: #f6f6f6;
    --ink: #262626;
    --ink-soft: #3a3a3a;
  }
  * { margin: 0; padding: 0; box-sizing: border-box; }
  html, body {
    width: 1200px;
    height: 900px;
    overflow: hidden;
    background: var(--backdrop);
    font-family: "Open Sans", Arial, sans-serif;
  }
  .card {
    position: absolute;
    left: 300px;
    width: 600px;
    height: 366px;
    box-shadow: 0 10px 28px rgba(0,0,0,0.35);
  }

  /* Back side */
  .card-back {
    top: 50px;
    background: linear-gradient(135deg, var(--brand-red) 0%, var(--brand-red-dark) 100%);
  }
  .card-back .wordmark {
    position: absolute;
    left: 90px;
    top: 200px;
    display: flex;
    align-items: center;
    gap: 16px;
  }
  .card-back .mark-dot {
    width: 44px;
    height: 44px;
    border-radius: 50%;
    background: var(--silver);
  }
  .card-back .brand-name {
    font-size: 64px;
    font-weight: 700;
    line-height: 1;
    color: var(--silver);
    letter-spacing: -1px;
  }
  .card-back .tagline {
    position: absolute;
    left: 150px;
    top: 272px;
    font-size: 15px;
    font-weight: 700;
    letter-spacing: 0.5px;
    color: var(--silver);
  }

  /* Front side */
  .card-front {
    top: 486px;
    background: var(--card-white);
    color: var(--ink);
  }
  .card-front .wordmark {
    position: absolute;
    right: 40px;
    top: 40px;
    display: flex;
    align-items: center;
    gap: 12px;
  }
  .card-front .mark-dot {
    width: 34px;
    height: 34px;
    border-radius: 50%;
    background: var(--brand-red);
  }
  .card-front .brand-name {
    font-size: 48px;
    font-weight: 700;
    line-height: 1;
    color: var(--ink);
    letter-spacing: -1px;
  }
  .card-front .tagline {
    position: absolute;
    right: 40px;
    top: 96px;
    font-size: 12px;
    font-weight: 700;
    letter-spacing: 0.4px;
    color: var(--ink);
  }
  .staff {
    position: absolute;
    left: 56px;
    top: 170px;
  }
  .staff-name {
    font-size: 22px;
    font-weight: 400;
    letter-spacing: 0.5px;
    color: var(--ink-soft);
  }
  .staff-role {
    font-size: 15px;
    color: var(--ink-soft);
  }
  .contact-rule {
    position: absolute;
    left: 300px;
    top: 190px;
    width: 2px;
    height: 150px;
    background: var(--brand-red);
  }
  .contact {
    position: absolute;
    left: 318px;
    top: 190px;
    font-size: 16px;
    line-height: 1.3;
    color: var(--ink-soft);
  }
  .contact-row { display: flex; gap: 14px; }
  .contact-label {
    width: 12px;
    font-weight: 700;
    color: var(--brand-red);
  }
  .address { margin-top: 14px; }
  .website { font-weight: 700; color: var(--ink); }
  .website .accent { color: var(--brand-red); }
</style>
</head>
<body>

<section class="card card-back" aria-label="Card back">
  <div class="wordmark">
    <span class="mark-dot"></span>
    <span class="brand-name">Velquora</span>
  </div>
  <div class="tagline">CLOUD MANAGED SERVICES</div>
</section>

<section class="card card-front" aria-label="Card front">
  <div class="wordmark">
    <span class="mark-dot"></span>
    <span class="brand-name">Velquora</span>
  </div>
  <div class="tagline">CLOUD MANAGED SERVICES</div>

  <div class="staff">
    <div class="staff-name">MARISA KELLNER</div>
    <div class="staff-role">Director</div>
  </div>

  <div class="contact-rule"></div>
  <div class="contact">
    <div class="contact-row"><span class="contact-label">M</span><span>0452 987 654</span></div>
    <div class="contact-row"><span class="contact-label">E</span><span>first.lastname@velquora.com</span></div>
    <div class="address">Suite 5, 48 Marlowe Lane,<br>Sydney NSW 2000</div>
    <div class="website">www.<span class="accent">velquora</span>.com</div>
  </div>
</section>

</body>
</html>
```